Smart Repair / Spot Repair neues Design neuer Name
Zielgruppe
Wir beseitigen Kleinschäden, sprich Beschädigungen , Kratzer ect. an Stoßstangen, Karosserieteilen, Felgen ... ect.) an Fahrzeugen, kostengünstig mit Spot Repair (besser bekannt als Smart Repair).
Besonders im Bereich für Gebrauchtwagen Aufbereitung und für Leasingrückläufer.
Wir haben bereits eine Facebook Seite über diese man sich evtl auch noch mehr Informationen veranschaulichen könnte. (KBV Kolbeck Blitzfein Dienst)
Aufgabenstellung
Für führen keine Reparaturen, wie in einer Autowerkstatt durch, d.h. es sollten keine typischen Werkzeuge oder ähnliches im Logo zu sehen sein.
Das Kürzel KBV soll NICHT mehr vorkommen.

```html
<!DOCTYPE html>
<html lang="de">
<head>
<meta charset="utf-8">
<title>Glanzwerk – Smart Repair Service</title>
<link rel="stylesheet" href="https://fonts.googleapis.com/css2?family=Arimo:wght@400;700&display=swap">
<style>
  :root {
    --gold: #a07a35;
    --gold-light: #b28a3f;
    --wine: #7a1416;
    --slate: #2f3333;
    --paper: #ffffff;
    --card-line: #5a4520;
  }
  * { box-sizing: border-box; margin: 0; padding: 0; }
  html, body { width: 848px; height: 1200px; overflow: hidden; background: var(--paper); }
  body { font-family: "Arimo", Arial, sans-serif; position: relative; }

  .hero-band {
    position: absolute; left: 0; top: 0; width: 848px; height: 328px;
    background: var(--gold);
    display: flex; flex-direction: column; align-items: center; justify-content: center;
  }
  .showcase-band {
    position: absolute; left: 0; top: 328px; width: 848px; height: 541px;
    background: var(--slate);
  }
  .flat-row { position: absolute; top: 925px; left: 0; width: 848px; }

  .wordmark {
    display: flex; align-items: center; gap: 12px;
    color: var(--wine); font-weight: 700; text-transform: uppercase; line-height: 1;
  }
  .wordmark-dot { border-radius: 50%; background: var(--wine); flex: none; }
  .tagline {
    color: var(--paper); text-transform: uppercase; font-weight: 400;
  }

  .hero-band .wordmark { font-size: 52px; letter-spacing: 1px; }
  .hero-band .wordmark-dot { width: 22px; height: 22px; }
  .hero-band .tagline { font-size: 11px; letter-spacing: 6px; margin-top: 18px; }

  .card {
    position: absolute; width: 344px; height: 222px;
    background: var(--gold); border: 1px solid var(--card-line);
  }
  .showcase-band .card { box-shadow: 0 10px 22px rgba(0,0,0,.45); }
  .card-front { display: flex; flex-direction: column; align-items: center; justify-content: center; }
  .card-front .wordmark { font-size: 30px; gap: 8px; }
  .card-front .wordmark-dot { width: 13px; height: 13px; }
  .card-front .tagline { font-size: 6.5px; letter-spacing: 3.5px; margin-top: 10px; }

  .card-back .brand { position: absolute; top: 60px; left: 0; width: 100%;
    display: flex; flex-direction: column; align-items: center; }
  .card-back .wordmark { font-size: 21px; gap: 6px; }
  .card-back .wordmark-dot { width: 9px; height: 9px; }
  .card-back .tagline { font-size: 4.5px; letter-spacing: 2.5px; margin-top: 7px; }

  .holder { position: absolute; left: 18px; top: 120px; color: var(--paper); }
  .holder-name { font-size: 11.5px; font-weight: 700; }
  .holder-role { font-size: 9.5px; }

  .contact { position: absolute; left: 195px; top: 120px; color: var(--wine); font-size: 9.5px; line-height: 13.3px; font-style: normal; }
  .contact-company { font-weight: 700; }
</style>
</head>
<body>

<header class="hero-band">
  <div class="wordmark"><span class="wordmark-dot"></span><span>Glanzwerk</span></div>
  <p class="tagline">Smart Repair Service</p>
</header>

<section class="showcase-band">
  <article class="card card-back" style="left:190px; top:60px;">
    <div class="brand">
      <div class="wordmark"><span class="wordmark-dot"></span><span>Glanzwerk</span></div>
      <p class="tagline">Smart Repair Service</p>
    </div>
    <div class="holder">
      <p class="holder-name">Max Mustermann</p>
      <p class="holder-role">Geschäftsführer</p>
    </div>
    <address class="contact">
      <p class="contact-company">Glanzwerk GmbH</p>
      <p>Musterstraße 123</p>
      <p>123456 Musterstadt in M.</p>
      <p>T&nbsp; + 49 1234 123 45 67</p>
      <p>M + 49 123 345 67 890</p>
      <p>m.mustermann@glanzwerk.de</p>
      <p>www.glanzwerk.de</p>
    </address>
  </article>
  <article class="card card-front" style="left:330px; top:250px;">
    <div class="wordmark"><span class="wordmark-dot"></span><span>Glanzwerk</span></div>
    <p class="tagline">Smart Repair Service</p>
  </article>
</section>

<section class="flat-row">
  <article class="card card-front" style="left:51px; top:0;">
    <div class="wordmark"><span class="wordmark-dot"></span><span>Glanzwerk</span></div>
    <p class="tagline">Smart Repair Service</p>
  </article>
  <article class="card card-back" style="left:453px; top:0;">
    <div class="brand">
      <div class="wordmark"><span class="wordmark-dot"></span><span>Glanzwerk</span></div>
      <p class="tagline">Smart Repair Service</p>
    </div>
    <div class="holder">
      <p class="holder-name">Max Mustermann</p>
      <p class="holder-role">Geschäftsführer</p>
    </div>
    <address class="contact">
      <p class="contact-company">Glanzwerk GmbH</p>
      <p>Musterstraße 123</p>
      <p>123456 Musterstadt in M.</p>
      <p>T&nbsp; + 49 1234 123 45 67</p>
      <p>M + 49 123 345 67 890</p>
      <p>m.mustermann@glanzwerk.de</p>
      <p>www.glanzwerk.de</p>
    </address>
  </article>
</section>

</body>
</html>
```